Pamphlet for IT Services Company (MSP Provider or Managed Services Provider)

We need a pamphlet designed for our Managed Services Company. We are an established company of 17 years that has never advertised. We'd like a pamphlet that we can drop off at potential client sites that describes our services. I like clean and prefer Orange as an accent color. We'd like to touch on the fact that we cater to our clients needs and go above and beyond what the other providers do.

Target Market(s)

Small and Medium Sized Businesses

Industry/Entity Type

It Service

Font styles to use
Other font styles liked:
• Try to match font on logo or website

Requirements
Must have
• Must highlight with the following Services and descriptions with Logo
Managed IT Services
IT Support
VOIP Solutions
WiFI Solutions
Contact information with phone number and website address.
Please view website korvanetpro.com
try to match fons on website above.
Nice to have
• Customer Testimonials. May a couple one line testimonials. Not real sure because this is the first time we've ever designed a brochure.
Should not have
• Not Sure

```html
<!DOCTYPE html>
<html lang="en">
<head>
<meta charset="utf-8">
<title>Korvanet Technologies – Managed IT Services</title>
<link href="https://fonts.googleapis.com/css2?family=Rajdhani:wght@500;600;700&family=Open+Sans:ital,wght@0,400;0,600;0,700;1,600&display=swap" rel="stylesheet">
<style>
  :root {
    --navy: #232b38;
    --navy-deep: #1a212c;
    --orange: #f47a1f;
    --orange-dark: #d9620e;
    --white: #ffffff;
    --paper: #f4f5f7;
    --grey: #5d6470;
    --grey-light: #c9cdd3;
    --hex-grey: #4a5260;
  }
  * { box-sizing: border-box; margin: 0; padding: 0; }
  html, body { width: 889px; height: 1200px; overflow: hidden; }
  body { font-family: "Open Sans", Arial, sans-serif; background: var(--paper); }

  .flyer { position: relative; width: 889px; height: 1200px; overflow: hidden; background: var(--white); }

  .hero { position: absolute; left: 0; top: 0; width: 889px; height: 400px; background: var(--navy); }

  .brand { position: absolute; left: 40px; top: 34px; display: flex; align-items: center; gap: 12px; }
  .brand-mark { width: 34px; height: 34px; border-radius: 50%; background: var(--orange); }
  .brand-name { font-family: "Rajdhani", sans-serif; font-weight: 600; font-size: 34px; color: var(--white); letter-spacing: .5px; }

  .headline { position: absolute; left: 40px; top: 140px; font-family: "Rajdhani", sans-serif; font-weight: 700; line-height: .95; font-size: 66px; text-transform: uppercase; }
  .headline .accent { color: var(--orange); display: block; }
  .headline .main { color: var(--white); display: block; }

  .tagline-band { position: absolute; left: 0; top: 284px; width: 470px; height: 106px; background: var(--orange); padding: 14px 30px 14px 40px; }
  .tagline { font-family: "Rajdhani", sans-serif; font-weight: 700; font-size: 25px; line-height: 1.02; color: var(--white); text-transform: uppercase; }
  .tagline-sub { margin-top: 8px; font-style: italic; font-weight: 600; font-size: 12px; line-height: 1.3; color: var(--navy); text-transform: uppercase; }

  .photo-hex { position: absolute; clip-path: polygon(25% 0, 75% 0, 100% 50%, 75% 100%, 25% 100%, 0 50%); }
  .photo-hex.frame { background: var(--orange); }
  .hex-office { left: 468px; top: 30px; width: 410px; height: 355px; background: linear-gradient(135deg, #e9ecef 0%, #b9c0c8 45%, #6c7480 100%); }
  .hex-office-frame { left: 462px; top: 24px; width: 422px; height: 367px; }
  .hex-vr { left: 610px; top: 360px; width: 250px; height: 216px; background: linear-gradient(160deg, #c7cdd4 0%, #7d8692 50%, #2f3642 100%); }
  .hex-vr-frame { left: 604px; top: 354px; width: 262px; height: 228px; }
  .hex-chip { left: 440px; top: 470px; width: 205px; height: 178px; background: linear-gradient(135deg, #3b6d4a 0%, #8a9a6a 45%, #2b3038 100%); }
  .hex-chip-frame { left: 434px; top: 464px; width: 217px; height: 190px; }

  .services { position: absolute; left: 0; top: 400px; width: 430px; height: 480px; padding: 26px 0 0 36px; background: var(--paper); }
  .service { display: flex; gap: 18px; margin-bottom: 20px; }
  .service-icon { flex: none; width: 70px; height: 62px; }
  .service-title { font-family: "Rajdhani", sans-serif; font-weight: 700; font-size: 19px; color: var(--orange); text-transform: uppercase; line-height: 1.1; }
  .service-text { margin-top: 3px; font-size: 10.5px; line-height: 1.4; color: var(--grey); max-width: 290px; }

  .testimonials { position: absolute; left: 660px; top: 600px; width: 210px; }
  .testimonial { display: flex; gap: 10px; margin-bottom: 26px; align-items: flex-start; }
  .quote-mark { font-family: "Rajdhani", sans-serif; font-weight: 700; font-size: 64px; line-height: .7; color: var(--orange); }
  .quote-text { font-size: 11px; line-height: 1.4; color: var(--grey); border-bottom: 2px solid var(--orange); padding-bottom: 6px; }

  .partners { position: absolute; left: 0; top: 892px; width: 889px; height: 80px; display: flex; justify-content: space-around; align-items: center; padding: 0 30px; border-top: 1px solid var(--grey-light); }
  .partner-badge { width: 104px; height: 30px; border-radius: 4px; background: var(--grey-light); }
  .partner-badge.round { width: 40px; height: 40px; border-radius: 50%; }

  .footer { position: absolute; left: 0; top: 980px; width: 889px; height: 220px; background: var(--navy-deep); border-top: 6px solid var(--orange); display: flex; align-items: center; justify-content: space-between; padding: 0 44px; }
  .contact { display: flex; align-items: center; gap: 14px; }
  .contact-icon { width: 54px; height: 54px; border-radius: 50%; background: var(--orange); display: flex; align-items: center; justify-content: center; }
  .contact-label { font-family: "Rajdhani", sans-serif; font-weight: 600; font-size: 18px; color: var(--white); text-transform: uppercase; letter-spacing: 1px; }
  .contact-value { font-family: "Rajdhani", sans-serif; font-weight: 700; font-size: 36px; color: var(--orange); line-height: 1; text-transform: uppercase; }
  .social-label { font-family: "Rajdhani", sans-serif; font-weight: 600; font-size: 18px; color: var(--white); margin-bottom: 8px; }
  .social-row { display: flex; gap: 10px; }
  .social-dot { width: 28px; height: 28px; border-radius: 4px; background: var(--orange); }
</style>
</head>
<body>
<main class="flyer">

  <section class="hero">
    <div class="brand">
      <span class="brand-mark"></span>
      <span class="brand-name">korvanet technologies</span>
    </div>

    <h1 class="headline">
      <span class="accent">Managed</span>
      <span class="main">IT Services</span>
    </h1>

    <div class="tagline-band">
      <p class="tagline">A simple, cost effective plan for your IT infrastructure.</p>
      <p class="tagline-sub">“Wouldn't it be nice if your stuff just worked?”</p>
    </div>
  </section>

  <div class="photo-hex frame hex-office-frame"></div>
  <div class="photo-hex hex-office" role="img" aria-label="Photo of a professional woman in glasses working at a laptop in a bright office"></div>

  <section class="services">
    <article class="service">
      <svg class="service-icon" viewBox="0 0 70 62" aria-hidden="true">
        <polygon points="17,1 53,1 69,31 53,61 17,61 1,31" fill="var(--hex-grey)"/>
        <path d="M35 15 L48 20 V31 C48 40 42 45 35 48 C28 45 22 40 22 31 V20 Z" fill="var(--white)"/>
      </svg>
      <div>
        <h2 class="service-title">Managed IT Services</h2>
        <p class="service-text">Let us take care of your IT. Our MSP is a flat rate service that includes onsite &amp; remote support, endpoint protection, web filtering, encrypted online backup &amp; patch management.</p>
      </div>
    </article>

    <article class="service">
      <svg class="service-icon" viewBox="0 0 70 62" aria-hidden="true">
        <polygon points="17,1 53,1 69,31 53,61 17,61 1,31" fill="var(--hex-grey)"/>
        <circle cx="35" cy="23" r="8" fill="var(--white)"/>
        <path d="M21 46 C21 36 28 33 35 33 C42 33 49 36 49 46 Z" fill="var(--white)"/>
      </svg>
      <div>
        <h2 class="service-title">IT Support</h2>
        <p class="service-text">We have a passion for what we do and it shows! Korvanet provides fast, reliable, expert solutions from experienced staff. You will never feel like just a client to us because our customers are family!</p>
      </div>
    </article>

    <article class="service">
      <svg class="service-icon" viewBox="0 0 70 62" aria-hidden="true">
        <polygon points="17,1 53,1 69,31 53,61 17,61 1,31" fill="var(--orange)"/>
        <path d="M26 17 L31 16 L34 24 L30 27 C32 32 35 35 40 37 L43 33 L51 36 L50 41 C48 45 42 46 36 42 C30 38 25 32 23 26 C22 21 23 18 26 17 Z" fill="var(--white)"/>
      </svg>
      <div>
        <h2 class="service-title">VOIP Solutions</h2>
        <p class="service-text">Let us take care of your phones. Our hosted voice plans include call routing, voicemail to email, mobile apps and conferencing for a low monthly rate.</p>
      </div>
    </article>

    <article class="service">
      <svg class="service-icon" viewBox="0 0 70 62" aria-hidden="true">
        <polygon points="17,1 53,1 69,31 53,61 17,61 1,31" fill="var(--hex-grey)"/>
        <g fill="none" stroke="var(--white)" stroke-width="3.5" stroke-linecap="round">
          <path d="M21 27 A20 20 0 0 1 49 27"/>
          <path d="M26 33 A13 13 0 0 1 44 33"/>
          <path d="M31 39 A6 6 0 0 1 39 39"/>
        </g>
        <circle cx="35" cy="45" r="3" fill="var(--white)"/>
      </svg>
      <div>
        <h2 class="service-title">WiFi Solutions</h2>
        <p class="service-text">WiFi is everywhere (at least it should be). Korvanet can extend your WiFi to cover your whole campus.</p>
      </div>
    </article>
  </section>

  <div class="photo-hex frame hex-vr-frame"></div>
  <div class="photo-hex hex-vr" role="img" aria-label="Photo of a woman wearing a virtual reality headset"></div>
  <div class="photo-hex frame hex-chip-frame"></div>
  <div class="photo-hex hex-chip" role="img" aria-label="Close-up photo of a circuit board with a processor chip"></div>

  <section class="testimonials">
    <blockquote class="testimonial">
      <span class="quote-mark">“</span>
      <p class="quote-text">Lorem ipsum dolor sit amet, consectetur adipiscing elit</p>
    </blockquote>
    <blockquote class="testimonial">
      <span class="quote-mark">“</span>
      <p class="quote-text">Lorem ipsum dolor sit amet, consectetur adipiscing elit</p>
    </blockquote>
    <blockquote class="testimonial">
      <span class="quote-mark">“</span>
      <p class="quote-text">Lorem ipsum dolor sit amet, consectetur adipiscing elit</p>
    </blockquote>
  </section>

  <section class="partners" aria-label="Technology partners">
    <span class="partner-badge round"></span>
    <span class="partner-badge"></span>
    <span class="partner-badge"></span>
    <span class="partner-badge"></span>
    <span class="partner-badge round"></span>
    <span class="partner-badge"></span>
  </section>

  <footer class="footer">
    <div class="contact">
      <span class="contact-icon">
        <svg width="26" height="26" viewBox="0 0 30 30" aria-hidden="true">
          <path d="M6 3 L11 2 L14 10 L10 13 C12 18 15 21 20 23 L23 19 L30 22 L29 27 C27 30 21 30 15 26 C9 22 4 16 2 10 C1 6 3 4 6 3 Z" fill="var(--white)"/>
        </svg>
      </span>
      <div>
        <p class="contact-label">Call us on</p>
        <p class="contact-value">0491 555 018</p>
      </div>
    </div>

    <div class="contact">
      <span class="contact-icon">
        <svg width="28" height="28" viewBox="0 0 30 30" aria-hidden="true">
          <g fill="none" stroke="var(--white)" stroke-width="2.2">
            <circle cx="15" cy="15" r="12"/>
            <ellipse cx="15" cy="15" rx="5" ry="12"/>
            <line x1="3" y1="15" x2="27" y2="15"/>
          </g>
        </svg>
      </span>
      <div>
        <p class="contact-label">Visit us on</p>
        <p class="contact-value">korvanetpro.com</p>
      </div>
    </div>

    <div class="social">
      <p class="social-label">Follow us on</p>
      <div class="social-row">
        <span class="social-dot"></span>
        <span class="social-dot"></span>
        <span class="social-dot"></span>
      </div>
    </div>
  </footer>

</main>
</body>
</html>
```